Business Card Re-Design/Update

We'd like to update out business cards. I've included our current "Style guide" which has the colour scheme of the organisation in it. I've also included the branding files with logos etc in them.

I've also included a copy of one of our existing cards so that you can see how ugly/dated they look. I'd like a fresh modern corporate look.

Target Market(s)

These are for our clients, potential clients, industry contacts - like all business cards

Contact Information for Business Card

Name
Position
Company Address - Level 1, 52 Copperfield Road, Dunmore Qld 4071
Direct Phone
mobile
Email
Website -www.korvelit.com.au
Logo

Colors

Designer to choose colors to be used in the design.

Requirements
Must have
• Main Logo
• Cards will need to be editable to be able to personalize them for each new employee.
Nice to have
• The MapIT, HandIT, KeepIT would be okay to have if they can be sensibly and professionally added to the look without detracting from the main imagery.
• Maybe they could go on the back of the card? will leave this to your creative discretion as to whether/where they fit.
Should not have
• Should not have decorative or script fonts

```html
<!DOCTYPE html>
<html lang="en">
<head>
<meta charset="utf-8">
<title>korvelIT business card</title>
<link rel="stylesheet" href="https://fonts.googleapis.com/css2?family=Arimo:wght@400;700&display=swap">
<style>
  :root {
    --brand-red: #d3202e;
    --ink-grey: #555659;
    --text-grey: #4a4a4c;
    --rule-dark: #3a3a3c;
    --card-white: #f6f6f6;
    --card-dark-top: #3b3b3d;
    --card-dark-bottom: #1e1e20;
    --page-bg: #d9d9db;
  }
  * { margin: 0; padding: 0; box-sizing: border-box; }
  html, body {
    width: 1200px; height: 900px; overflow: hidden;
    background: var(--page-bg);
    font-family: "Arimo", Arial, sans-serif;
  }
  .sheet {
    width: 1200px; height: 900px;
    display: flex; flex-direction: column; align-items: center; justify-content: center;
    gap: 40px;
  }
  .card {
    position: relative;
    width: 720px; height: 400px;
    box-shadow: 0 6px 18px rgba(0,0,0,.18);
    overflow: hidden;
  }
  /* Front */
  .card-front { background: linear-gradient(160deg, #ffffff 0%, var(--card-white) 60%, #ececec 100%); }
  .brand {
    position: absolute; display: flex; align-items: center; gap: 16px;
  }
  .card-front .brand { left: 150px; top: 62px; }
  .brand-square { width: 58px; height: 58px; background: var(--brand-red); }
  .brand-name {
    font-weight: 700; font-size: 74px; letter-spacing: -1px; line-height: 1;
    color: var(--ink-grey);
  }
  .divider {
    position: absolute; left: 0; right: 0; top: 232px; height: 1px; background: var(--rule-dark);
  }
  .divider-accent {
    position: absolute; left: 0; width: 270px; top: 231px; height: 3px; background: var(--brand-red);
  }
  .person { position: absolute; left: 44px; top: 168px; }
  .person-name { color: var(--brand-red); font-weight: 700; font-size: 22px; }
  .person-title { color: var(--text-grey); font-size: 15px; margin-top: 4px; }
  .contacts { position: absolute; left: 44px; top: 252px; list-style: none; }
  .contacts li {
    display: flex; align-items: center; gap: 10px;
    color: var(--text-grey); font-size: 15px; line-height: 23px;
  }
  .contacts svg { width: 14px; height: 14px; fill: var(--brand-red); flex: none; }
  .address {
    position: absolute; right: 40px; bottom: 34px; text-align: right;
    color: var(--text-grey); font-size: 15px; line-height: 21px;
  }
  /* Back */
  .card-back {
    background: radial-gradient(ellipse at 50% 30%, var(--card-dark-top) 0%, var(--card-dark-bottom) 85%);
    display: flex; align-items: center; justify-content: center;
  }
  .card-back .brand { position: static; }
  .card-back .brand-name { color: #e4e4e6; }
</style>
</head>
<body>
<main class="sheet">
  <section class="card card-front" aria-label="Card front">
    <div class="brand">
      <span class="brand-square"></span>
      <span class="brand-name">korvelIT</span>
    </div>

    <div class="person">
      <div class="person-name">Dana Whitfield</div>
      <div class="person-title">Business Development Manager</div>
    </div>

    <div class="divider"></div>
    <div class="divider-accent"></div>

    <ul class="contacts">
      <li>
        <svg viewBox="0 0 16 16" aria-hidden="true"><rect x="1" y="5" width="14" height="10" rx="1"/><rect x="3" y="1" width="10" height="3" rx="1"/></svg>
        +61 (0) 7 3000 4182
      </li>
      <li>
        <svg viewBox="0 0 16 16" aria-hidden="true"><rect x="4" y="0" width="8" height="16" rx="2"/></svg>
        +61 (0) 400 555 219
      </li>
      <li>
        <svg viewBox="0 0 16 16" aria-hidden="true"><path d="M0 3h16v10H0z M0 3l8 6 8-6" stroke="#fff" stroke-width="1"/></svg>
        dwhitfield@korvelit.com.au
      </li>
      <li>
        <svg viewBox="0 0 16 16" aria-hidden="true"><circle cx="8" cy="8" r="7.5"/><path d="M0.5 8h15M8 0.5v15M2.5 4.5h11M2.5 11.5h11" stroke="#fff" stroke-width="1" fill="none"/></svg>
        www.korvelit.com.au
      </li>
    </ul>

    <div class="address">Level 1, 52 Copperfield Road,<br>Dunmore Qld 4071</div>
  </section>

  <section class="card card-back" aria-label="Card back">
    <div class="brand">
      <span class="brand-square"></span>
      <span class="brand-name">korvelIT</span>
    </div>
  </section>
</main>
</body>
</html>
```